Pagecraft Design Project - Vibrant Children's school bag website

We need a fresh design for the landing page of our new web site and blog: quillonmarket.com

Tamborine specialises in supplying schools all over the world and now also parents directly with, personalised school bags, accessories, crafts and gifts for their children.

I have attached the visual that our web designers have provided so that we can see the layout of the various window, but now we need to add the personal touch of making it our own and visually making the site look enticing and exciting to shop on.
Updates

Hello Designers,

We are now in the final round of choosing a design.  We have found that most deisgns are very similar and that none are completley original.  Therefore, we are willing to throw our wire frame away and start with a compleltely new visual so you can design what ever you like!

The only requirements we have is that we must have:
- A large rolling banner to show our products lines
- Our Company logo
- Meta going tags across the top
- Icons for chatterbook,snipboard,blog,
- Account Login bar
- A log in area for schools
- A login area to register for the Club Tambo

So we are looking for something that really stands out from the crowd!

can you deliver?

Thanks,

Target Market(s)

To appeal to mum's shopping on line for their children's school items and gifts.

Industry/Entity Type

School

Requirements
Must have
• -When you see the visual attached please note the amendments:
- the word 'school bags' under our company name will not appear
- the tag line "Australia's no 1 specialist school bag company' should be deleted. We will leave this area open so that you can include some simple icons that we would like featured across the top of the banner i.e:
- a love heart icon + wording to say : Made with love
- A 'delivery' icon + wording to say : Free delivery
- A 'warranty' icon + wording to say : up to 25 year warranty
- A 'world' icon + wording to say : we ship to the universe
(Please see: www.pebblecrate.com.au for reference of what we mean!)

We we want the overall design to be clean, fresh, crisp and fun to look at.

You may alter the colours of everything, even the coloured tabs. we think that the coloured tabs should actually just be one colour through out and to let the tamborine name stand out with all it's.

The top/main photo will be a rolling banner.

You can change the shapes of the boxes but keep to the wire frame.

Please alter the design of the black/coloured club tambo card to suit your design.

Our aim is to also change the side panels in peak seasons to reflect halloween banner, christmas banner etc.

Please see my screen shot of the current page and see where the "dots' pattern sits on either side of the shopping panels. Please include the side panels as we want to change the design to have themes i.e for halloween, for christmas etc etc.

example of websites that have this:

http://www.wavemoorly.com/

Please include a 'blog' and snipboard icon.

The site will not only manage our retail sales but will also be a portal for our schools to register and place their bulk orders with us. So the "wholesale register box" must stand out so our school customers can easily see where they need to click & register.
Should not have
• Please do not do a 'baby' boutique theme. We need a theme that appeals to mum's that have children across the ages of 3-14 years.

```html
<!DOCTYPE html>
<html lang="en">
<head>
<meta charset="utf-8">
<title>Tamborine – School Bags</title>
<link rel="stylesheet" href="https://fonts.googleapis.com/css2?family=Ubuntu:wght@400;500;700&family=Arimo:wght@400;700&display=swap">
<style>
:root{
  --page:#e6e2da;
  --white:#ffffff;
  --sky:#1ab0ea;
  --orange:#f7941d;
  --yellow:#ffc90e;
  --lime:#8cc63f;
  --pink:#ec008c;
  --purple:#7b2fb5;
  --link:#1a8fd0;
  --text:#555555;
  --dark:#333333;
  --band:#3e3e3e;
  --foot-text:#e8e8e8;
  --arrow:#9acd32;
  --card:#cde9f3;
}
*{box-sizing:border-box;margin:0;padding:0}
html,body{width:1200px;height:1171px;overflow:hidden}
body{position:relative;background:var(--page);font-family:"Arimo",Arial,sans-serif;color:var(--text)}
.abs{position:absolute}

/* header */
.header{left:131px;top:0;width:935px;height:144px;background:var(--white)}
.logo{left:23px;top:14px;display:flex;align-items:center;gap:8px}
.logo-dot{width:22px;height:22px;border-radius:50%;background:var(--purple)}
.logo-name{font-family:"Ubuntu",sans-serif;font-weight:700;font-size:46px;color:var(--sky);letter-spacing:-1px}
.perk{top:28px;width:130px;text-align:center;font-family:"Ubuntu",sans-serif;font-size:11.5px;color:#444}
.perk svg{display:block;margin:0 auto 6px}
.nav{left:18px;top:103px;display:flex;gap:4px}
.nav a{display:block;height:34px;line-height:34px;padding:0 9px;background:var(--sky);color:#fff;font-size:12.5px;text-decoration:none}
.nav a.active{background:var(--orange)}
.nav-rule{left:0;top:138px;width:935px;height:4px;background:var(--orange)}

/* banner */
.banner{left:131px;top:155px;width:936px;height:298px;background:#fafafa;box-shadow:0 1px 3px rgba(0,0,0,.15)}
.banner-photo{position:absolute;left:8px;top:8px;width:922px;height:281px;
  background:linear-gradient(90deg,#9a8c6a 0%,#6f8a4a 30%,#c0392b 55%,#3f6fb0 75%,#8aa060 100%)}

/* panels */
.panel{background:var(--white);border-radius:12px;box-shadow:0 2px 4px rgba(0,0,0,.18)}
.panel-title{position:absolute;left:8px;top:8px;right:10px;height:33px;border-radius:9px;
  font-family:"Ubuntu",sans-serif;font-weight:700;font-size:17.5px;color:#fff;line-height:33px;padding-left:11px;letter-spacing:.3px}
.t-sky{background:var(--sky)}.t-yellow{background:var(--yellow)}.t-lime{background:var(--lime)}
.t-pink{background:var(--pink)}.t-purple{background:var(--purple)}.t-orange{background:var(--orange)}
.link-head{font-family:"Ubuntu",sans-serif;font-weight:500;color:var(--link);font-size:13.5px}
.copy{font-size:12px;line-height:15.5px;color:var(--text)}
.small{font-size:10.5px;line-height:12.5px;color:var(--text)}

.endorse{left:140px;top:480px;width:273px;height:253px}
.endorse-photo{left:14px;top:49px;width:248px;height:86px;background:linear-gradient(90deg,#e9d8c8,#f3ede8 45%,#c9a88e)}

.social{left:464px;top:480px;width:274px;height:252px}
.social-row{left:17px;display:flex;gap:8px}
.social-icon{width:45px;height:45px;border-radius:8px;flex:none}

.club{left:789px;top:477px;width:274px;height:252px}
.club-card{left:13px;top:47px;width:251px;height:92px;background:var(--card)}
.club-offer{position:absolute;left:6px;top:69px;width:242px;height:20px;background:var(--pink);color:#fff;font-family:"Ubuntu",sans-serif;font-weight:700;font-size:12px;line-height:20px;text-align:center}
.field{background:#fff;border:1px solid #ccc;border-radius:6px}
.btn{border-radius:7px;background:linear-gradient(180deg,#8a8a8a,#3f3f3f);color:#fff;font-family:"Ubuntu",sans-serif;font-weight:500;text-align:center;box-shadow:0 1px 2px rgba(0,0,0,.3)}

.community{left:142px;top:758px;width:273px;height:186px}
.badge{background:#e6e6e6}

.news{left:465px;top:758px;width:274px;height:186px}
.news-copy{font-size:12px;line-height:14px;color:var(--text)}

.schools{left:788px;top:758px;width:274px;height:186px}
.schools label{font-size:12px;color:#444}
.field-soft{border-radius:12px;background:linear-gradient(180deg,#eee,#fafafa);border:1px solid #d8d8d8}

/* footer */
.footer{left:0;top:983px;width:1200px;height:188px;background:var(--dark)}
.footer-band{left:0;top:12px;width:1200px;height:27px;background:var(--band)}
.foot-head{top:20px;font-family:"Ubuntu",sans-serif;font-weight:700;font-size:11.5px;color:#fff}
.foot-list{list-style:none;font-family:"Ubuntu",sans-serif;font-size:12px;color:var(--foot-text)}
.foot-list li{height:19.2px}
.foot-list li::before{content:"»";color:var(--arrow);margin-right:5px;font-weight:700}
.foot-sep{top:52px;width:1px;height:98px;background:#555}
.copyright{left:0;top:172px;width:1200px;text-align:center;font-family:"Ubuntu",sans-serif;font-size:11px;color:#9a9a9a}
</style>
</head>
<body>

<header class="abs header">
  <div class="abs logo"><span class="logo-name">tamborine</span><span class="logo-dot"></span></div>

  <div class="abs perk" style="left:317px">
    <svg width="30" height="26" viewBox="0 0 30 26"><path d="M15 25 L3 13 A7 7 0 0 1 15 5 A7 7 0 0 1 27 13 Z" fill="#f7941d"/></svg>Made with love</div>
  <div class="abs perk" style="left:418px">
    <svg width="30" height="26" viewBox="0 0 30 26"><rect x="2" y="5" width="26" height="18" rx="2" fill="#f7941d"/><path d="M2 6 L15 16 L28 6" stroke="#fff" stroke-width="2" fill="none"/></svg>Free Delivery</div>
  <div class="abs perk" style="left:544px">
    <svg width="34" height="26" viewBox="0 0 34 26"><circle cx="17" cy="12" r="11" fill="#e07b16"/><rect x="5" y="15" width="24" height="7" rx="2" fill="#8b4513"/></svg>Up to 25 year warranty</div>
  <div class="abs perk" style="left:695px">
    <svg width="30" height="26" viewBox="0 0 30 26"><circle cx="15" cy="13" r="11" fill="none" stroke="#f7941d" stroke-width="2"/><circle cx="11" cy="10" r="1.6" fill="#f7941d"/><circle cx="19" cy="10" r="1.6" fill="#f7941d"/><path d="M9 15 Q15 21 21 15" stroke="#f7941d" stroke-width="2" fill="none"/></svg>We ship to the universe</div>

  <nav class="abs nav">
    <a href="#">Test Menu</a><a href="#">Kids Backpacks</a><a href="#" class="active">Kids Bags</a>
    <a href="#" style="padding:0 15px">Sports</a><a href="#">Kids Clothing</a><a href="#" style="padding:0 13px">Art &amp; Craft</a>
    <a href="#" style="padding:0 12px">Music</a><a href="#" style="padding:0 4px">Kids Diaries</a><a href="#">Kids Storage</a>
    <a href="#">Extra Stuff</a><a href="#" style="padding:0 16px 0 13px">Sale</a>
  </nav>
  <div class="abs nav-rule"></div>
</header>

<section class="abs banner">
  <div class="banner-photo" role="img" aria-label="Rolling banner photo: children outdoors wearing colourful school backpacks"></div>
</section>

<section class="abs panel endorse">
  <h2 class="panel-title t-sky">Endorsements</h2>
  <div class="abs endorse-photo" role="img" aria-label="Photo of a doctor examining a young girl"></div>
  <div class="abs link-head" style="left:14px;top:153px">Dr Lena Marsh</div>
  <p class="abs copy" style="left:14px;top:172px;width:250px">Contrary to popular belief, Lorem Ipsum is not simply random text. It has roots in a piece of classical Latin literature from 45 BC, making it over 2000 years old.</p>
</section>

<section class="abs panel social">
  <h2 class="panel-title t-yellow">Say To Tamborine</h2>
  <div class="abs social-row" style="top:54px"><div class="social-icon" style="background:#3b5b98"></div>
    <div><div class="link-head">Follow us Chatterbook</div><p class="small">There are many variations of pass-<br>ages of Lorem Ipsum available.</p></div></div>
  <div class="abs social-row" style="top:111px"><div class="social-icon" style="background:#3fb6e6"></div>
    <div><div class="link-head">Follow us Chirpline</div><p class="small">There are many variations of pass-<br>ages of Lorem Ipsum available.</p></div></div>
  <div class="abs social-row" style="top:168px"><div class="social-icon" style="background:#dddddd"></div>
    <div><div class="link-head">Follow us Vidstream</div><p class="small">There are many variations of pass-<br>ages of Lorem Ipsum available.</p></div></div>
  <p class="abs" style="left:21px;top:235px;font-size:12px;color:#444">Join now for 15% off your first order!</p>
</section>

<section class="abs panel club">
  <h2 class="panel-title t-lime">Club Tambo</h2>
  <div class="abs club-card" role="img" aria-label="Club membership card artwork">
    <div class="club-offer">Join now for 15% off your first order!</div>
  </div>
  <span class="abs" style="left:13px;top:152px;font-family:Ubuntu,sans-serif;font-size:14px;color:#444">Email:</span>
  <div class="abs field" style="left:61px;top:148px;width:183px;height:25px"></div>
  <div class="abs btn" style="left:163px;top:185px;width:79px;height:20px;font-size:11.5px;line-height:20px">Join Now</div>
</section>

<section class="abs panel community">
  <h2 class="panel-title t-pink">Community</h2>
  <div class="abs badge" role="img" aria-label="Partner charity badge" style="left:18px;top:55px;width:116px;height:58px;border-radius:8px"></div>
  <div class="abs badge" role="img" aria-label="Partner charity badge" style="left:148px;top:55px;width:112px;height:58px;border-radius:8px"></div>
  <div class="abs badge" role="img" aria-label="Partner charity badge" style="left:58px;top:120px;width:150px;height:58px;border-radius:8px"></div>
</section>

<section class="abs panel news">
  <h2 class="panel-title t-purple">News &amp; Blog</h2>
  <div class="abs link-head" style="left:15px;top:55px">Headline 1</div>
  <p class="abs news-copy" style="left:15px;top:71px;width:256px">Contrary to popular belief, Lorem Ipsum is not simply random text. It has roots in a piece of classical .</p>
  <div class="abs link-head" style="left:15px;top:119px">Headline 1</div>
  <p class="abs news-copy" style="left:15px;top:135px;width:256px">Contrary to popular belief, Lorem Ipsum is not simply random text. It has roots in a piece of classical .</p>
  <span class="abs" style="left:196px;top:173px;font-family:Ubuntu,sans-serif;font-size:12px;color:#666">read more »</span>
</section>

<section class="abs panel schools">
  <h2 class="panel-title t-orange">Schools &amp; Resellers Reg</h2>
  <label class="abs" style="left:21px;top:74px">Username :</label>
  <div class="abs field-soft" style="left:87px;top:66px;width:145px;height:25px"></div>
  <label class="abs" style="left:21px;top:106px">Password :</label>
  <div class="abs field-soft" style="left:87px;top:99px;width:145px;height:25px"></div>
  <div class="abs btn" style="left:122px;top:137px;width:122px;height:25px;font-size:14px;line-height:25px">Register Now</div>
</section>

<footer class="abs footer">
  <div class="abs footer-band"></div>
  <div class="abs foot-head" style="left:193px">PEBBLECRATE GUARANTEE</div>
  <div class="abs foot-head" style="left:380px">OUR STORY</div>
  <div class="abs foot-head" style="left:554px">MOST SHOPPED</div>
  <div class="abs foot-head" style="left:727px">BIRD TALK</div>
  <div class="abs foot-head" style="left:885px">TOP BRANDS</div>

  <ul class="abs foot-list" style="left:190px;top:53px"><li>Delivery Guarantee</li><li>Pricing Guarantee</li><li>Privacy Guarantee</li><li>Return Guarantee</li><li>Security Guarantee</li></ul>
  <ul class="abs foot-list" style="left:372px;top:53px"><li>Delivery Guarantee</li><li>Pricing Guarantee</li><li>Privacy Guarantee</li><li>Return Guarantee</li><li>Security Guarantee</li></ul>
  <ul class="abs foot-list" style="left:549px;top:52px"><li>Delivery Guarantee</li><li>Pricing Guarantee</li><li>Privacy Guarantee</li><li>Return Guarantee</li><li>Security Guarantee</li></ul>
  <ul class="abs foot-list" style="left:720px;top:50px"><li>Delivery Guarantee</li><li>Pricing Guarantee</li><li>Privacy Guarantee</li><li>Return Guarantee</li><li>Security Guarantee</li></ul>
  <ul class="abs foot-list" style="left:880px;top:49px"><li>Delivery Guarantee</li><li>Pricing Guarantee</li><li>Privacy Guarantee</li><li>Return Guarantee</li><li>Security Guarantee</li></ul>

  <div class="abs foot-sep" style="left:342px"></div>
  <div class="abs foot-sep" style="left:520px"></div>
  <div class="abs foot-sep" style="left:693px"></div>
  <div class="abs foot-sep" style="left:856px"></div>

  <p class="abs copyright">© 2012 Wattle Lane, Inc. All rights reserved.</p>
</footer>

</body>
</html>
```